Allied Health business card / Logo update.

Update/revitalise our logo and business cards. The logo needs to be suitable not only for business cards but stationary, website and clothing as well.

We have had the same hand logo for 16 years and have a strong brand name with this. One idea, however, was to base the idea around the similarities between the spine and bamboo. I will attach some images.

We are uncertain with colour. Initially, we thought earthy greens and greys/charcoal. However, we would also consider blue/charcoal combination.

I have attached our existing logo and this is our website. http://www.harbourleafspinal.com.au

Target Market(s)

General public
This is the only card

Industry/Entity Type

Health Care

Contact Information for Business Card

Harbourleaf Chiropractic Centre
27 Willowmere Road (Cnr Banfield St and Willowmere Rd) Port Ellison
4/58 Thornbury St Kelsmore
phone: 02 6571 4826
email: info@harbourleafspinal.com.au
web: harbourleafspinal.com.au

Marcus P. Helton
Cert. Rehab Therapist
Chiropractor
BSc(Ash)., MChirop(Lin)., MClinRehabNeuro(Bry)
MCPA, MANRS, TIVA

Font styles to use
Serif
Sans Serif

Colors
acd037
85acd3
5c5c5c

Requirements
Must have
• Company name, Professional name with qualifications
• Contact details.

```html
<!DOCTYPE html>
<html lang="en">
<head>
<meta charset="utf-8">
<title>Harbourleaf Chiropractic Centre – Business Card</title>
<link href="https://fonts.googleapis.com/css2?family=Arimo:wght@400;700&display=swap" rel="stylesheet">
<style>
  :root {
    --page: #e9e6e1;
    --card: #ffffff;
    --orange: #ec7023;
    --ink: #1d1d1d;
    --ink-soft: #3a3a3a;
  }
  * { margin: 0; padding: 0; box-sizing: border-box; }
  html, body { width: 1200px; height: 892px; overflow: hidden; }
  body {
    background: var(--page);
    font-family: "Arimo", Arial, sans-serif;
    position: relative;
  }
  .card {
    position: absolute;
    left: 280px;
    width: 640px;
    height: 366px;
    box-shadow: 0 6px 18px rgba(0,0,0,0.18);
    overflow: hidden;
  }
  .card-front { top: 50px; background: var(--card); }
  .card-back { top: 470px; }

  .front-logo {
    position: absolute;
    left: 40px;
    top: 58px;
    display: flex;
    align-items: center;
    gap: 12px;
  }
  .front-logo .mark {
    width: 40px; height: 40px; border-radius: 50%;
    background: var(--orange);
    flex: none;
  }
  .front-logo .wordmark {
    color: var(--orange);
    font-weight: 700;
    font-size: 26px;
    line-height: 1.1;
    width: 200px;
  }
  .divider { position: absolute; left: 0; top: 0; }

  .practitioner {
    position: absolute;
    left: 350px;
    top: 34px;
    color: var(--ink);
  }
  .practitioner .name { font-size: 30px; font-weight: 400; margin-bottom: 6px; }
  .practitioner .role { font-size: 17px; line-height: 1.2; color: var(--ink-soft); }
  .practitioner .quals { font-size: 12px; line-height: 1.35; color: var(--ink-soft); margin-top: 2px; }

  .contact {
    position: absolute;
    left: 336px;
    top: 168px;
    list-style: none;
    color: var(--ink);
    font-size: 16px;
  }
  .contact li { display: flex; align-items: center; gap: 8px; height: 22px; }
  .contact .icon {
    width: 16px; height: 16px; background: var(--orange);
    border-radius: 3px; display: flex; align-items: center; justify-content: center;
    flex: none;
  }

  .address-band {
    position: absolute;
    left: 0; bottom: 0;
    width: 100%; height: 104px;
    background: var(--orange);
    color: #fff;
    font-size: 19px;
    line-height: 1.35;
    padding: 22px 0 0 40px;
  }

  .back-image {
    position: absolute; inset: 0;
    background:
      linear-gradient(90deg, #bfc2bd 0%, #8e918c 12%, #5d5d5d 22%, #7a7a7a 50%, #5a5a5a 80%, #8a8d88 100%);
  }
  .back-image::after {
    content: ""; position: absolute; left: 22%; right: 0; top: 18%; bottom: 18%;
    background: radial-gradient(ellipse at 55% 50%, rgba(230,230,230,0.55), rgba(120,120,120,0.1) 70%);
  }
  .back-logo {
    position: absolute;
    left: 140px; top: 140px;
    display: flex; align-items: center; gap: 14px;
  }
  .back-logo .mark { width: 56px; height: 56px; border-radius: 50%; background: var(--orange); flex: none; }
  .back-logo .wordmark { color: var(--orange); font-weight: 700; font-size: 34px; line-height: 1.1; width: 360px; }
</style>
</head>
<body>

<section class="card card-front" aria-label="Business card front">
  <svg class="divider" width="640" height="366" aria-hidden="true">
    <line x1="290" y1="262" x2="340" y2="120" stroke="#ec7023" stroke-width="2"/>
  </svg>

  <div class="front-logo">
    <span class="mark"></span>
    <span class="wordmark">Harbourleaf Chiropractic Centre</span>
  </div>

  <div class="practitioner">
    <p class="name">Marcus P. Helton</p>
    <p class="role">Cert. Rehab Therapist</p>
    <p class="role">Chiropractor</p>
    <p class="quals">BSc(Ash)., MChirop(Lin).,<br>MClinRehabNeuro(Bry)<br>MCPA, MANRS, TIVA</p>
  </div>

  <ul class="contact">
    <li>
      <span class="icon"><svg width="10" height="10" viewBox="0 0 10 10"><path d="M2 1 L4 1 L4.5 3 L3.3 4 Q4.2 5.8 6 6.7 L7 5.5 L9 6 L9 8 Q9 9 8 9 Q1 8.5 1 2 Q1 1 2 1Z" fill="#fff"/></svg></span>
      02 6571 4826
    </li>
    <li>
      <span class="icon"><svg width="11" height="8" viewBox="0 0 11 8"><rect x="0.5" y="0.5" width="10" height="7" fill="none" stroke="#fff"/><path d="M0.5 0.5 L5.5 4.5 L10.5 0.5" fill="none" stroke="#fff"/></svg></span>
      info@harbourleafspinal.com.au
    </li>
    <li>
      <span class="icon"><svg width="10" height="10" viewBox="0 0 10 10"><circle cx="5" cy="5" r="4" fill="none" stroke="#fff"/><ellipse cx="5" cy="5" rx="1.8" ry="4" fill="none" stroke="#fff"/><line x1="1" y1="5" x2="9" y2="5" stroke="#fff"/></svg></span>
      harbourleafspinal.com.au
    </li>
  </ul>

  <div class="address-band">
    <p>27 Willowmere Road (Cnr Banfield St and Willowmere Rd)</p>
    <p>Port Ellison 4/58 Thornbury St Kelsmore</p>
  </div>
</section>

<section class="card card-back" aria-label="Business card back">
  <div class="back-image" role="img" aria-label="Monochrome photograph of bamboo stalks beside a spinal x-ray"></div>
  <div class="back-logo">
    <span class="mark"></span>
    <span class="wordmark">Harbourleaf Chiropractic Centre</span>
  </div>
</section>

</body>
</html>
```